Simple and clean

We need a business card design for a new company called Dwelling Owl. It is a search engine to find current properties for sale or rent in New Zealand market.
We have already a colour scheme that we would like people to use.
Light brown: #D4CCB0
Light green: #D6E4D4
Green: #669966
Black/White
It is OK to divert from this colour scheme slightly as long as there is a green component to the business card.
Final design should be clean, simple and should communicate the nature of the business.
Target Market(s)
- First home buyers
- Real estate agents
- People seeking rentals
Industry/Entity Type
Business
Requirements
Must have
- Use those or similar colours.
Light brown: #D4CCB0
Light green: #D6E4D4
Green: #669966
Black/White

```html
<!DOCTYPE html>
<html lang="en">
<head>
<meta charset="utf-8">
<title>Dwelling Owl – Business Card</title>
<link rel="stylesheet" href="https://fonts.googleapis.com/css2?family=Poppins:wght@300;400;600&display=swap">
<style>
  :root {
    --backdrop: #1e1e1e;
    --card: #ffffff;
    --card-shade: #ececec;
    --light-brown: #d4ccb0;
    --light-green: #d6e4d4;
    --green: #669966;
    --muted-green: #7a9a7a;
    --ink: #222222;
    --white: #ffffff;
  }
  * { margin: 0; padding: 0; box-sizing: border-box; }
  html, body {
    width: 1200px;
    height: 852px;
    overflow: hidden;
    background: var(--backdrop);
    font-family: "Poppins", sans-serif;
  }
  .card {
    position: absolute;
    left: 130px;
    top: 156px;
    width: 940px;
    height: 540px;
    border-radius: 30px;
    overflow: hidden;
    background: linear-gradient(180deg, var(--card) 0%, var(--card-shade) 100%);
  }
  .corner-decoration {
    position: absolute;
    left: 0;
    top: 0;
    width: 200px;
    height: 320px;
    background: radial-gradient(ellipse at 30% 40%, rgba(214, 228, 212, 0.85) 0%, rgba(214, 228, 212, 0.35) 55%, rgba(214, 228, 212, 0) 80%);
  }
  .brand {
    position: absolute;
    top: 62px;
    right: 62px;
    display: flex;
    align-items: center;
    gap: 20px;
  }
  .brand-mark {
    width: 50px;
    height: 50px;
    background: var(--green);
  }
  .brand-name {
    font-size: 56px;
    font-weight: 600;
    letter-spacing: -0.5px;
    color: var(--ink);
    text-transform: uppercase;
    line-height: 1;
  }
  .wave {
    position: absolute;
    left: 0;
    top: 0;
    width: 940px;
    height: 540px;
  }
  .wave-trim { fill: var(--light-brown); }
  .wave-band { fill: var(--green); }
  .person {
    position: absolute;
    left: 64px;
    top: 292px;
  }
  .person-name {
    font-size: 48px;
    font-weight: 300;
    color: var(--green);
    line-height: 1.1;
  }
  .person-role {
    font-size: 22px;
    font-weight: 300;
    letter-spacing: 4px;
    color: var(--muted-green);
    line-height: 1.2;
    margin-top: 2px;
  }
  .contacts {
    position: absolute;
    right: 64px;
    top: 398px;
    list-style: none;
    text-align: right;
    color: var(--white);
    font-size: 20px;
    font-weight: 300;
    line-height: 38px;
  }
  .contact-label {
    font-weight: 600;
    margin-right: 6px;
  }
</style>
</head>
<body>
  <div class="card">
    <div class="corner-decoration" role="img" aria-label="Faint light green decorative motif in the upper left corner"></div>

    <div class="brand">
      <span class="brand-mark"></span>
      <span class="brand-name">Dwelling Owl</span>
    </div>

    <svg class="wave" viewBox="0 0 940 540" aria-hidden="true">
      <path class="wave-trim" d="M0 392 C 120 432, 260 452, 420 422 C 600 388, 760 312, 940 300 L 940 540 L 0 540 Z"/>
      <path class="wave-band" d="M0 408 C 120 448, 260 468, 420 438 C 600 404, 760 328, 940 316 L 940 540 L 0 540 Z"/>
    </svg>

    <div class="person">
      <p class="person-name">Rowan Kettle</p>
      <p class="person-role">director</p>
    </div>

    <ul class="contacts">
      <li><span class="contact-label">mobile</span>555 - 010 - 233</li>
      <li><span class="contact-label">email</span>mail@dwellingowl.com</li>
      <li><span class="contact-label">web</span>www.dwellingowl.co.nz</li>
    </ul>
  </div>
</body>
</html>
```